An Iconic transformation in mattress design and comfort.

“An iconic transformation in mattress design and comfort”
We are Not Kidding here!!
This is an upstart Company, PIRZO7, LLC
Our Slogan
“dream-PIRZO”

We need an outstanding web design for an outstanding product.

It took 8 years to design this bed. It was originally designed by its owner for its owner, I continue to use it every day.

With our innovative patent pending support system, with quality throughout, simplicity in design, affordable, and proudly made here in the USA, we offer a product that is superior to anything that is in the market place now. The materials that are used deviate from the industry standard, and for good reason, our product feels incredibly plush, soft, but yet provides support that can be adjusted in a simple manor, a product that will last a lifetime.
Really, why go to work if you can lay in this bed all day; you'll want to work from home! A quick nap, you'll be in heaven.

Overall Web design:
We like the web site “taltrunex.com”, sleek, modern, a site that seems to add credibility to their product by issuing registration numbers for their tops, not a bad idea for our beds. Its important to understand that this industry is filled with smoke and mirrors, over pricing, very poor quality, and show rooms filled with sales people that are piranhas.; we seek to distance ourselves! This company will sell its product not in the traditional show room but online. Please also see these websites: www.brimvora.com, www.nudlet.com

Last thing I want to see is a another website filled with beds, what to do? Well perhaps a few shots of our beds is ok, after all thats what we are selling. An idea here; I was listening to a news show, this man decided to tell his story with tattoos on his own body! Interesting, different approach (not that I'm into tattoos); website design with innovation through simplicity and creative thinking and marketing.

The photos of our product have yet to be taken by a professional. We have yet to find a way to photograph this product in a different and innovative manner.

Target Market(s)

Millennials

Industry/Entity Type

It Company

Number of Pages Required

4 page

Font styles to use
Serif

Colors
ec1f27

Requirements
Must have
• Existing logo
Nice to have
• See project description
• Can further expand upon, upon request for specifics.
Should not have
• See project description

```html
<!DOCTYPE html>
<html lang="en">
<head>
<meta charset="utf-8">
<title>Pirzo7 — Mattress Design and Comfort</title>
<link href="https://fonts.googleapis.com/css2?family=Jost:ital,wght@0,300;0,400;0,500;1,400&display=swap" rel="stylesheet">
<style>
:root{
  --red:#ec1f27;
  --ink:#1a1a1a;
  --text:#333;
  --muted:#8a8a8a;
  --rule:#d0d0d0;
  --soft:#f6f6f6;
  --black:#0b0b0b;
  --white:#fff;
}
*{box-sizing:border-box;margin:0;padding:0}
html,body{width:1200px;height:2812px;overflow:hidden}
body{font-family:"Jost",sans-serif;color:var(--text);background:var(--white);position:relative}
section,header,footer,.topbar{position:absolute;left:0;width:1200px}
.abs{position:absolute}
.red{color:var(--red)}

.topbar{top:0;height:38px;background:var(--black);color:#ddd;font-size:12px;letter-spacing:.6px}
.topbar .quote{left:156px;top:11px;font-style:italic}
.topbar .divider{left:643px;top:0;width:1px;height:38px;background:#444}
.topbar .account{right:156px;top:11px;display:flex;gap:14px}
.topbar .account .sep{color:#777}

.site-header{top:38px;height:97px;background:var(--white);box-shadow:0 1px 3px rgba(0,0,0,.08)}
.brand{left:156px;top:16px}
.brand-name{font-size:40px;font-weight:500;color:var(--ink);line-height:1;letter-spacing:-.5px}
.brand-tag{font-size:11px;color:var(--ink);margin-left:48px;margin-top:2px}
.main-nav{left:405px;top:40px;display:flex;gap:28px;font-size:13px;color:var(--ink)}
.main-nav .active{color:var(--red)}
.main-nav .phone{display:flex;align-items:center;gap:6px;margin-left:8px;letter-spacing:.5px}

.hero{top:135px;height:358px;background:linear-gradient(180deg,#5b4a3d 0%,#3c332d 45%,#2b2b2d 100%)}
.hero-photo{left:0;top:0;width:1200px;height:358px;background:radial-gradient(ellipse at 50% 55%,rgba(120,118,122,.55),rgba(40,32,28,.2) 70%)}
.hero-title{top:112px;width:100%;text-align:center;color:var(--white);font-size:38px;font-weight:400;letter-spacing:.5px}
.hero-sub{top:158px;width:100%;text-align:center;color:#eee;font-size:15px}
.btn-shop{left:543px;top:203px;width:114px;height:32px;border-radius:16px;background:var(--red);color:var(--white);font-size:12px;text-align:center;line-height:32px}
.hero-arrow{top:160px;width:38px;height:38px;border-radius:50%;display:flex;align-items:center;justify-content:center}
.hero-arrow.prev{left:60px;border:2px solid var(--red);background:rgba(0,0,0,.4)}
.hero-arrow.next{left:1067px;background:var(--red)}

.section-title{width:100%;text-align:center;font-size:29px;font-weight:400;color:var(--ink)}
.title-rule{left:580px;width:40px;height:1px;background:var(--rule)}

.why{top:493px;height:435px}
.why .section-title{top:40px}
.why .title-rule{top:92px}
.why-photo{left:156px;top:126px;width:431px;height:261px;background:linear-gradient(160deg,#a58a6e,#e9e5dd 55%,#4b4b55)}
.features{left:636px;top:118px;width:380px}
.feature{display:flex;gap:18px;height:72px}
.feature svg{flex:none;margin-top:2px}
.feature h3{font-size:15px;line-height:18px;font-weight:400;color:var(--ink)}
.feature p{font-size:11px;color:var(--muted);line-height:17px;margin-top:1px}

.about{top:928px;height:379px;background:var(--soft)}
.about h2{left:156px;top:78px;font-size:30px;font-weight:400;color:var(--ink)}
.about .rule{left:156px;top:126px;width:40px;height:1px;background:var(--rule)}
.about p{left:156px;top:144px;width:380px;font-size:11.5px;line-height:19px;color:var(--muted)}
.btn-more{left:156px;top:260px;width:113px;height:34px;border:1.5px solid var(--red);border-radius:17px;font-size:12px;text-align:center;line-height:31px;color:var(--ink)}
.video{left:611px;top:49px;width:432px;height:279px;background:linear-gradient(180deg,#6a5545,#2e2a28 55%,#3a3a40)}
.video .play{left:191px;top:93px}
.video .caption{top:155px;width:100%;text-align:center;color:var(--white);font-size:19px}

.gallery{top:1307px;height:611px}
.gallery .section-title{top:40px}
.gallery .title-rule{top:92px}
.gallery-grid{left:156px;top:122px;width:888px;height:442px;display:grid;grid-template-columns:repeat(4,222px);grid-template-rows:repeat(2,221px)}
.tile{position:relative}
.tile.featured{background:linear-gradient(#d8636a,#e22b35)}
.tile.featured .cap{position:absolute;top:58px;width:100%;text-align:center;color:var(--white)}
.tile.featured h4{font-size:16px;font-weight:400}
.tile.featured .line{width:40px;height:1px;background:#fff;margin:10px auto}
.tile.featured p{font-size:11.5px;line-height:15px}
.tile.featured svg{margin-top:12px}

.reviews{top:1918px;height:520px;background:var(--soft)}
.reviews .section-title{top:40px}
.reviews .title-rule{top:92px}
.review{top:126px;width:280px;height:300px;background:var(--white);text-align:center}
.review .mark{margin-top:30px}
.review blockquote{margin:16px auto 0;width:200px;font-size:13px;line-height:20px;color:var(--muted)}
.review .stars{margin-top:20px;display:flex;justify-content:center;gap:3px}
.review .name{margin-top:18px;font-size:14px;color:var(--ink)}
.review .role{font-size:11px;color:var(--muted)}
.avatar{left:100px;top:262px;width:80px;height:80px;border-radius:50%;background:linear-gradient(#c9b7a9,#8c7a70);border:4px solid #fff;box-shadow:0 2px 6px rgba(0,0,0,.2)}
.rv-arrow{top:290px}

.newsletter{top:2438px;height:326px}
.kicker{top:50px;width:100%;text-align:center;font-size:11px;letter-spacing:1.4px;color:var(--ink)}
.newsletter .title-rule{top:70px;left:585px;width:30px}
.newsletter h2{top:78px;width:100%;text-align:center;font-size:29px;font-weight:400;color:var(--ink)}
.newsletter .sub{top:115px;width:100%;text-align:center;font-size:14px;color:var(--muted)}
.subscribe{left:437px;top:161px;display:flex}
.subscribe .field{width:285px;height:32px;border:1px solid #ccc;font-size:11px;font-style:italic;color:#777;padding:9px 12px}
.subscribe .send{width:41px;height:32px;background:var(--red);display:flex;align-items:center;justify-content:center}
.follow{top:222px;width:100%;text-align:center;font-size:12px;letter-spacing:1.4px;color:var(--ink)}
.social{left:536px;top:252px;display:flex;gap:10px}
.social span{width:26px;height:26px;border-radius:50%;background:var(--black)}
.social span.hi{background:var(--red)}
.address{left:156px;top:255px;font-size:12px;line-height:15px;color:var(--ink);display:flex;gap:8px}
.help{right:156px;top:255px;font-size:12px;line-height:16px;color:var(--ink);text-align:right}

.site-footer{top:2764px;height:48px;background:var(--black)}
.site-footer .copy{left:156px;top:16px;color:#ddd;font-size:12px}
.site-footer .totop{left:1021px;top:14px}
</style>
</head>
<body>

<div class="topbar">
  <div class="abs quote">"An iconic transformation in mattress design and comfort"</div>
  <div class="abs divider"></div>
  <div class="abs account"><span class="red">Register</span><span class="sep">|</span><span>Login</span><span class="sep">|</span><span>Cart Item &nbsp;$0.00</span></div>
</div>

<header class="site-header">
  <div class="abs brand">
    <div class="brand-name">Pirzo7</div>
    <div class="brand-tag">Dream-Pirzo</div>
  </div>
  <nav class="abs main-nav">
    <span class="active">Home</span><span>Why Choose Us?</span><span>Gallery</span><span>Quality</span><span>Store</span><span>Contact Us</span>
    <span class="phone"><svg width="11" height="11" viewBox="0 0 24 24"><path d="M6.6 10.8a15.1 15.1 0 0 0 6.6 6.6l2.2-2.2c.3-.3.7-.4 1-.2 1.1.4 2.300.6 3.6.6.6 0 1 .4 1 1V20c0 .6-.4 1-1 1A17 17 0 0 1 3 4c0-.6.4-1 1-1h3.5c.6 0 1 .4 1 1 0 1.3.2 2.5.6 3.6.1.3 0 .7-.2 1z" fill="#1a1a1a"/></svg>555.014.7720</span>
  </nav>
</header>

<section class="hero">
  <div class="abs hero-photo" role="img" aria-label="Quilted grey and white mattress on a floor in a living room"></div>
  <h1 class="abs hero-title">A Product That Will Last a Lifetime</h1>
  <div class="abs hero-sub">There are many variations of passages</div>
  <div class="abs btn-shop">Shop Now</div>
  <div class="abs hero-arrow prev"><svg width="14" height="14" viewBox="0 0 14 14"><path d="M12 7H2M6 3L2 7l4 4" stroke="#fff" stroke-width="1.8" fill="none"/></svg></div>
  <div class="abs hero-arrow next"><svg width="14" height="14" viewBox="0 0 14 14"><path d="M2 7h10M8 3l4 4-4 4" stroke="#fff" stroke-width="1.8" fill="none"/></svg></div>
</section>

<section class="why">
  <h2 class="abs section-title">Why <span class="red">Choose Us?</span></h2>
  <div class="abs title-rule"></div>
  <div class="abs why-photo" role="img" aria-label="White mattress on a grey quilted base in a bedroom"></div>
  <div class="abs features">
    <div class="feature">
      <svg width="34" height="34" viewBox="0 0 34 34"><circle cx="17" cy="17" r="14" fill="none" stroke="#aaa" stroke-width="2"/><text x="17" y="21" font-size="10" text-anchor="middle" fill="#aaa" font-family="Jost,sans-serif">24</text></svg>
      <div><h3>Support system</h3><p>There are many variations of passages of Lorem Ipsum available, but the majority have suffered.</p></div>
    </div>
    <div class="feature">
      <svg width="34" height="34" viewBox="0 0 34 34"><circle cx="17" cy="15" r="10" fill="none" stroke="#aaa" stroke-width="2" stroke-dasharray="3 2"/><circle cx="17" cy="15" r="5" fill="#aaa"/><path d="M12 24l-3 8 5-2 3 3 0-7M22 24l3 8-5-2-3 3" fill="#aaa"/></svg>
      <div><h3>Quality throughout</h3><p>There are many variations of passages of Lorem Ipsum available, but the majority have suffered.</p></div>
    </div>
    <div class="feature">
      <svg width="34" height="34" viewBox="0 0 34 34"><rect x="5" y="9" width="24" height="16" fill="none" stroke="#aaa" stroke-width="2"/><circle cx="17" cy="17" r="4" fill="none" stroke="#aaa" stroke-width="2"/><path d="M2 12v16h24" fill="none" stroke="#aaa" stroke-width="2"/></svg>
      <div><h3>Affordable</h3><p>There are many variations of passages of Lorem Ipsum available, but the majority have suffered.</p></div>
    </div>
    <div class="feature">
      <svg width="34" height="34" viewBox="0 0 34 34"><path d="M3 31V14l7 5v-5l7 5v-5l7 5V4h5v27z" fill="#aaa"/></svg>
      <div><h3>industry standard</h3><p>There are many variations of passages of Lorem Ipsum available, but the majority have suffered.</p></div>
    </div>
  </div>
</section>

<section class="about">
  <h2 class="abs">About <span class="red">Pirzo7</span></h2>
  <div class="abs rule"></div>
  <p class="abs">At vero eos et accusamus et iusto odio dignissimos ducimus qui blanditiis praesentium voluptatum deleniti atque corrupti quos dolores et quas molestias excepturi sint occaecati cupiditate non provident, similique sunt in culpa qui officia deserunt mollitia animi, id est laborum et dolorum fuga...</p>
  <div class="abs btn-more">More About</div>
  <div class="abs video" role="img" aria-label="Video still of a quilted mattress in a room with a fireplace">
    <svg class="abs play" width="50" height="50" viewBox="0 0 50 50"><circle cx="25" cy="25" r="23" fill="none" stroke="#fff" stroke-width="2"/><path d="M20 15l14 10-14 10z" fill="#fff"/></svg>
    <div class="abs caption">Our Manufacturing Process!</div>
  </div>
</section>

<section class="gallery">
  <h2 class="abs section-title">Photo <span class="red">Gallery</span></h2>
  <div class="abs title-rule"></div>
  <div class="abs gallery-grid">
    <div class="tile" role="img" aria-label="White sofa with green cushions" style="background:linear-gradient(135deg,#8fb06a,#e8e6e0 60%,#c9c3b8)"></div>
    <div class="tile featured">
      <div class="cap">
        <h4>Righteous Indignation</h4>
        <div class="line"></div>
        <p>dislike men who are so<br>beguiled and.</p>
        <svg width="18" height="18" viewBox="0 0 18 18"><path d="M10 2h6v6M16 2l-6 6M8 16H2v-6M2 16l6-6" stroke="#fff" stroke-width="1.8" fill="none"/></svg>
      </div>
    </div>
    <div class="tile" role="img" aria-label="Layered mattress with brown pillows" style="background:linear-gradient(180deg,#e4e0dc,#8a7670 45%,#f0eeec)"></div>
    <div class="tile" role="img" aria-label="Thick pillow-top mattress in a grey studio" style="background:linear-gradient(180deg,#c9c9c9,#f4f4f4 50%,#b8b8b8)"></div>
    <div class="tile" role="img" aria-label="Stack of folded mattress toppers" style="background:linear-gradient(180deg,#f2f2f0,#b9b7b2 60%,#8c6f6a)"></div>
    <div class="tile" role="img" aria-label="Pile of white pillows" style="background:linear-gradient(160deg,#d9d2c6,#f3f0ea 55%,#c8c0b3)"></div>
    <div class="tile" role="img" aria-label="Tufted white futon mattress" style="background:linear-gradient(180deg,#9f8a66,#f5f2ea 40%,#e3dccd)"></div>
    <div class="tile" role="img" aria-label="Embroidered cream mattress on a bed frame" style="background:linear-gradient(180deg,#b79e7c,#efe6d4 50%,#8c6b4d)"></div>
  </div>
</section>

<section class="reviews">
  <h2 class="abs section-title">What Our <span class="red">Customers Say?</span></h2>
  <div class="abs title-rule"></div>
  <svg class="abs rv-arrow" style="left:80px" width="30" height="26" viewBox="0 0 30 26"><path d="M12 2L2 11l10 9v-5c7 0 12 2 16 8-1-9-6-15-16-16z" fill="#111"/></svg>
  <svg class="abs rv-arrow" style="left:1090px" width="30" height="26" viewBox="0 0 30 26"><path d="M18 2l10 9-10 9v-5C11 15 6 17 2 23 3 14 8 8 18 7z" fill="var(--red)"/></svg>

  <div class="abs review" style="left:156px">
    <svg class="mark" width="36" height="28" viewBox="0 0 36 28"><path d="M2 26V14C2 7 5 3 13 2l1 3c-5 1-7 4-7 8h6v13zM20 26V14c0-7 3-11 11-12l1 3c-5 1-7 4-7 8h6v13z" fill="none" stroke="#aaa" stroke-width="2"/></svg>
    <blockquote>"The mattress breathes nicely, which keeps the bed cool"</blockquote>
    <div class="stars"><svg width="80" height="14" viewBox="0 0 80 14"><g fill="#555"><path id="s" d="M7 1l1.8 4 4.2.4-3.2 2.8 1 4.2L7 10.2 3.2 12.4l1-4.2L1 5.4l4.2-.4z"/><use href="#s" x="16"/><use href="#s" x="32"/></g><use href="#s" x="48" fill="#555" opacity=".55"/><use href="#s" x="64" fill="none" stroke="#555"/></svg></div>
    <div class="name">Mara</div><div class="role">Even slightly</div>
    <div class="abs avatar" role="img" aria-label="Customer portrait"></div>
  </div>
  <div class="abs review" style="left:460px">
    <svg class="mark" width="36" height="28" viewBox="0 0 36 28"><path d="M2 26V14C2 7 5 3 13 2l1 3c-5 1-7 4-7 8h6v13zM20 26V14c0-7 3-11 11-12l1 3c-5 1-7 4-7 8h6v13z" fill="#555"/></svg>
    <blockquote>"Immediately noticed the difference in support &amp; comfort"</blockquote>
    <div class="stars"><svg width="80" height="14" viewBox="0 0 80 14"><g fill="#555"><use href="#s"/><use href="#s" x="16"/><use href="#s" x="32"/></g><use href="#s" x="48" fill="#555" opacity=".55"/><use href="#s" x="64" fill="none" stroke="#555"/></svg></div>
    <div class="name">Standard chunk</div><div class="role">Embarrassing</div>
    <div class="abs avatar" role="img" aria-label="Customer portrait"></div>
  </div>
  <div class="abs review" style="left:762px">
    <svg class="mark" width="36" height="28" viewBox="0 0 36 28"><path d="M2 26V14C2 7 5 3 13 2l1 3c-5 1-7 4-7 8h6v13zM20 26V14c0-7 3-11 11-12l1 3c-5 1-7 4-7 8h6v13z" fill="none" stroke="#aaa" stroke-width="2"/></svg>
    <blockquote>"I love this new mattress. Very comfortable and relaxed!"</blockquote>
    <div class="stars"><svg width="80" height="14" viewBox="0 0 80 14"><g fill="#555"><use href="#s"/><use href="#s" x="16"/><use href="#s" x="32"/></g><use href="#s" x="48" fill="#555" opacity=".55"/><use href="#s" x="64" fill="none" stroke="#555"/></svg></div>
    <div class="name">Odette</div><div class="role">Model sentence</div>
    <div class="abs avatar" role="img" aria-label="Customer portrait"></div>
  </div>
</section>

<section class="newsletter">
  <div class="abs kicker">JOIN THE PIRZO7</div>
  <div class="abs title-rule"></div>
  <h2 class="abs">Sign Up <span class="red">Newsletter</span></h2>
  <div class="abs sub">Subscribe to our newsletter to get latest scoop right to your inbox.</div>
  <div class="abs subscribe">
    <div class="field">Enter Your Email ...</div>
    <div class="send"><svg width="14" height="14" viewBox="0 0 14 14"><path d="M1 6l12-5-5 12-1.5-5z" fill="#fff"/></svg></div>
  </div>
  <div class="abs follow">FOLLOW US:</div>
  <div class="abs social"><span></span><span class="hi"></span><span></span><span></span></div>
  <div class="abs address">
    <svg width="10" height="14" viewBox="0 0 10 14"><path d="M5 0a5 5 0 0 1 5 5c0 4-5 9-5 9S0 9 0 5a5 5 0 0 1 5-5z" fill="var(--red)"/><circle cx="5" cy="5" r="2" fill="#fff"/></svg>
    <div>The standard chunk of Lorem Ipsum used<br>USA 123456</div>
  </div>
  <div class="abs help">Need help? Call Us: <span class="red">&#9742;</span> 555.014.7720<br>info@pirzo7.com</div>
</section>

<footer class="site-footer">
  <div class="abs copy">© 2016 Pirzo 7. All Rights Reserved.</div>
  <svg class="abs totop" width="20" height="20" viewBox="0 0 20 20"><path d="M10 2l8 9h-5v7H7v-7H2z" fill="var(--red)"/></svg>
</footer>

</body>
</html>
```